Zelvo - revolutionary mobile payment

The app is a P2P money trasfert, without the using of credit card or bank circuits it can transfer electronic money from one person to another consumers simply and immediatelly.
You can use the color you want, but the message we need to transert to consumer is simplicity, safety and coolness.
In attach the logo of the company and the wireframe of thre page of the app.
The goal is to design the page of the app with a clear, simple and intuitive graphic.
Updates

I have upgrade the brief with important information and detail, many thanks

Target Market(s)

all the people

Industry/Entity Type

Credit Card

Requirements
Must have
• You have to design one icon for each button in the first page, (shop is: where to shop)
in the second one a new intuitive image (instead of the hand) that let the user to understand that with a simple swipe he can process the payment
Nice to have
• You can include or esxclude what you want or belive can improve user experience of the app
Should not have
• too much color, too much button or information

```html
<!DOCTYPE html>
<html lang="it">
<head>
<meta charset="utf-8">
<title>Zelvo – app screens</title>
<link rel="stylesheet" href="https://fonts.googleapis.com/css2?family=Roboto:wght@300;400;500;700&display=swap">
<style>
:root{
  --page:#eceaef;
  --status:#0d0d0d;
  --topbar:#e9e9e9;
  --header:#2e2e2e;
  --backdrop-top:#5e514a;
  --backdrop-bottom:#37302c;
  --tile:rgba(38,36,35,.9);
  --row:rgba(34,33,32,.92);
  --key:rgba(35,28,24,.72);
  --key-line:rgba(120,100,90,.45);
  --brand:#1f3a78;
  --red:#b5232c;
  --green:#2c9a3f;
  --white:#ffffff;
  --muted:#cfcfcf;
}
*{box-sizing:border-box;margin:0;padding:0}
html,body{width:1200px;height:866px;overflow:hidden;background:var(--page);
  font-family:"Roboto",Arial,sans-serif;color:var(--white)}
.stage{position:relative;width:1200px;height:866px}
.screen{position:absolute;top:194px;width:300px;height:533px;overflow:hidden;background:var(--backdrop-bottom);
  transform:scale(.903);transform-origin:top left}
.screen--home{left:99px}.screen--pay{left:466px}.screen--balance{left:827px}

.backdrop{position:absolute;left:0;right:0;bottom:0;
  background:linear-gradient(180deg,var(--backdrop-top) 0%,var(--backdrop-bottom) 100%)}

.status{position:absolute;top:0;left:0;width:100%;height:22px;background:var(--status);
  font-size:10px;display:flex;align-items:center;justify-content:space-between;padding:0 8px}
.status__time{position:absolute;left:0;right:0;text-align:center;font-weight:500}
.status__left,.status__right{position:relative;z-index:1}
.status__right{display:flex;align-items:center;gap:4px}
.battery{width:20px;height:9px;border:1px solid #fff;border-radius:2px;padding:1px}
.battery i{display:block;width:22%;height:100%;background:#fff}

.topbar{position:absolute;top:22px;left:0;width:100%;height:32px;background:var(--topbar);
  display:flex;align-items:center;justify-content:space-between;padding:0 8px}
.brand{display:flex;align-items:center;gap:4px;color:var(--brand);font-weight:700;font-size:14px}
.brand__dot{width:13px;height:13px;border-radius:50%;background:var(--brand)}

.header{position:absolute;top:54px;left:0;width:100%;height:104px;background:var(--header);
  display:flex;align-items:center;padding:0 12px}
.avatar{width:66px;height:66px;border-radius:50%;border:3px solid #fff;
  background:linear-gradient(160deg,#c9b7a4,#7d6a5a);flex:none}
.profile{margin-left:12px}
.profile__name{font-size:16px;font-weight:500}
.profile__phone{font-size:10px;color:var(--muted);margin-top:3px}
.edit{margin-left:auto;width:22px;height:22px;border-radius:50%;background:#666;display:flex;align-items:center;justify-content:center}

.tile{position:absolute;width:116px;height:117px;background:var(--tile);display:flex;flex-direction:column;align-items:center;justify-content:center;gap:8px;font-size:13px;font-weight:500}
.tile svg{width:56px;height:50px}

.back{font-size:11px;color:#ddd}
.pay-header{height:65px;justify-content:center}
.pay-header .back{position:absolute;left:6px}
.pay-title{display:flex;align-items:center;gap:6px;font-size:20px;font-weight:500}

.field{position:absolute;left:40px;top:158px;width:219px;height:35px;background:#e6e6e6;color:#222;
  display:flex;align-items:center;font-size:12px;border:1px solid #bbb}
.field__icon{width:33px;height:100%;background:#fff;display:flex;align-items:center;justify-content:center;border-right:1px solid #bbb}
.field__code{font-weight:700;margin:0 5px 0 7px}
.currency{position:absolute;left:17px;top:228px;font-size:26px;font-weight:700}
.amount{position:absolute;left:48px;top:218px;width:235px;height:50px;background:#333;color:#fff;
  font-size:29px;font-weight:500;display:flex;align-items:center;justify-content:center;letter-spacing:1px}
.note{position:absolute;left:8px;top:290px;font-size:8px;background:#555;padding:2px 4px;color:#ddd}
.keypad{position:absolute;left:6px;top:308px;width:284px;height:217px;display:grid;
  grid-template-columns:repeat(3,1fr);grid-template-rows:repeat(4,1fr);gap:2px}
.key{background:var(--key);border:1px solid var(--key-line);display:flex;align-items:center;justify-content:center;font-size:22px;font-weight:400}

.balance-header .back{position:absolute;left:6px}
.saldo{margin-left:auto;margin-right:10px;text-align:right}
.saldo__label{font-size:11px}
.saldo__value{font-size:18px;font-weight:500}
.range{position:absolute;left:211px;top:176px;width:83px;height:15px;background:#222;font-size:7px;
  display:flex;align-items:center;justify-content:space-between;padding:0 5px}
.txn{position:absolute;left:37px;width:222px;height:29px;background:var(--row);display:flex;align-items:center;font-size:10px;padding:0 8px}
.txn__phone{margin-left:8px;width:108px}
.txn__amount{font-weight:700;width:50px}
.txn svg:last-child{margin-left:auto}
.btn{position:absolute;top:471px;width:106px;height:43px;display:flex;align-items:center;justify-content:center;font-size:13px;font-weight:500}
.btn--report{left:36px;background:var(--red)}
.btn--pockets{left:156px;background:var(--green)}
</style>
</head>
<body>
<main class="stage">

<!-- Home -->
<section class="screen screen--home">
  <div class="backdrop" style="top:158px" role="img" aria-label="Blurred background photo of a shop interior"></div>
  <div class="status"><span class="status__left">●●●○○ NOVA</span><span class="status__time">4:21 PM</span><span class="status__right">✱ 22% <span class="battery"><i></i></span></span></div>
  <div class="topbar">
    <svg width="20" height="20" viewBox="0 0 20 20"><circle cx="8" cy="11" r="5" fill="none" stroke="#333" stroke-width="3" stroke-dasharray="2.5 1.5"/><circle cx="15" cy="5" r="2.5" fill="none" stroke="#333" stroke-width="2"/></svg>
    <span class="brand"><span class="brand__dot"></span>Zelvo</span>
  </div>
  <header class="header">
    <div class="avatar" role="img" aria-label="Profile photo of the user"></div>
    <div class="profile"><div class="profile__name">Marco Lenti</div><div class="profile__phone">+39 320 555 0147</div></div>
    <span class="edit"><svg width="12" height="12" viewBox="0 0 12 12"><path d="M2 10l1-3 5-5 2 2-5 5z" fill="#fff"/></svg></span>
  </header>
  <a class="tile" style="left:24px;top:216px">
    <svg viewBox="0 0 56 50"><rect x="14" y="20" width="38" height="24" rx="2" fill="#fff"/><rect x="14" y="26" width="38" height="4" fill="#333"/><circle cx="42" cy="37" r="5" fill="#333"/><path d="M4 6q10 2 16 14l-8 6q-6-6-8-20z" fill="#fff"/></svg>Pay</a>
  <a class="tile" style="left:161px;top:216px">
    <svg viewBox="0 0 56 50"><path d="M4 22h14v8h20v-8h14v24H4z" fill="#fff"/><path d="M22 2h12v12h6L28 26 16 14h6z" fill="#fff"/><circle cx="44" cy="32" r="8" fill="#333" stroke="#fff" stroke-width="2"/></svg>Ask</a>
  <a class="tile" style="left:24px;top:355px">
    <svg viewBox="0 0 56 50"><circle cx="28" cy="11" r="10" fill="#fff"/><path d="M10 48v-14q0-10 18-10t18 10v14z" fill="#fff"/><path d="M26 25h4l-1 14h-2z" fill="#333"/></svg>Account</a>
  <a class="tile" style="left:161px;top:355px">
    <svg viewBox="0 0 56 50"><path d="M16 20L28 4l12 16" fill="none" stroke="#fff" stroke-width="3"/><path d="M4 20h48l-6 26H10z" fill="#fff"/><path d="M18 26v14M28 26v14M38 26v14" stroke="#333" stroke-width="3"/></svg>Shop</a>
</section>

<!-- Pay -->
<section class="screen screen--pay">
  <div class="backdrop" style="top:119px" role="img" aria-label="Blurred background photo of a shop interior"></div>
  <div class="status"><span class="status__left">●●●○○ NOVA</span><span class="status__time">4:21 PM</span><span class="status__right">✱ 22% <span class="battery"><i></i></span></span></div>
  <div class="topbar">
    <svg width="20" height="20" viewBox="0 0 20 20"><circle cx="8" cy="11" r="5" fill="none" stroke="#333" stroke-width="3" stroke-dasharray="2.5 1.5"/><circle cx="15" cy="5" r="2.5" fill="none" stroke="#333" stroke-width="2"/></svg>
    <span class="brand"><span class="brand__dot"></span>Zelvo</span>
  </div>
  <header class="header pay-header">
    <span class="back">‹ Indietro</span>
    <span class="pay-title"><svg width="26" height="28" viewBox="0 0 26 28"><path d="M3 6q10-6 20 0" fill="none" stroke="#fff" stroke-width="2"/><path d="M19 2l4 4-5 1" fill="none" stroke="#fff" stroke-width="2"/><path d="M10 10v10l-3-2-2 2 7 7h9l1-10-7-2v-5q0-2-2.5-2T10 10z" fill="#fff"/></svg>Pay</span>
  </header>
  <div class="field"><span class="field__icon"><svg width="12" height="20" viewBox="0 0 12 20"><rect x="1" y="1" width="10" height="18" rx="2" fill="none" stroke="#222" stroke-width="2"/></svg></span><span class="field__code">+39</span>Cellulare</div>
  <span class="currency">€</span>
  <div class="amount">851.33</div>
  <span class="note">Inserisci note (opzionale) ▾</span>
  <div class="keypad">
    <span class="key">1</span><span class="key">2</span><span class="key">3</span>
    <span class="key">4</span><span class="key">5</span><span class="key">6</span>
    <span class="key">7</span><span class="key">8</span><span class="key">9</span>
    <span class="key">.</span><span class="key">0</span>
    <span class="key"><svg width="24" height="16" viewBox="0 0 24 16"><path d="M7 0h17v16H7L0 8z" fill="#fff"/><path d="M11 4l8 8M19 4l-8 8" stroke="#333" stroke-width="2"/></svg></span>
  </div>
</section>

<!-- Balance -->
<section class="screen screen--balance">
  <div class="backdrop" style="top:158px" role="img" aria-label="Blurred background photo of a shop interior"></div>
  <div class="status"><span class="status__left">●●●○○ NOVA</span><span class="status__time">4:21 PM</span><span class="status__right">✱ 22% <span class="battery"><i></i></span></span></div>
  <div class="topbar">
    <svg width="20" height="20" viewBox="0 0 20 20"><circle cx="8" cy="11" r="5" fill="none" stroke="#333" stroke-width="3" stroke-dasharray="2.5 1.5"/><circle cx="15" cy="5" r="2.5" fill="none" stroke="#333" stroke-width="2"/></svg>
    <span class="brand"><span class="brand__dot"></span>Zelvo</span>
  </div>
  <header class="header balance-header">
    <span class="back">‹ Indietro</span>
    <div class="saldo"><div class="saldo__label">Il Tuo Saldo</div><div class="saldo__value">€106.82</div></div>
    <div class="avatar" role="img" aria-label="Profile photo of the user"></div>
  </header>
  <div class="range"><span>Ultimi 30 Giorni</span><span>▾</span></div>

  <div class="txn" style="top:201px"><svg width="14" height="12" viewBox="0 0 14 12"><path d="M7 0l7 6h-2v6H9V8H5v4H2V6H0z" fill="#fff"/></svg><span class="txn__phone">+39 340 555 0182</span><span class="txn__amount">€&nbsp;&nbsp;1</span><svg width="7" height="10" viewBox="0 0 7 10"><path d="M0 0l7 5-7 5z" fill="#fff"/></svg></div>
  <div class="txn" style="top:238px"><svg width="14" height="12" viewBox="0 0 14 12"><path d="M7 0l7 6h-2v6H9V8H5v4H2V6H0z" fill="#fff"/></svg><span class="txn__phone">+39 340 555 0182</span><span class="txn__amount">€&nbsp;&nbsp;-1</span><svg width="7" height="10" viewBox="0 0 7 10"><path d="M0 0l7 5-7 5z" fill="#fff"/></svg></div>
  <div class="txn" style="top:275px"><svg width="14" height="12" viewBox="0 0 14 12"><path d="M7 0l7 6h-2v6H9V8H5v4H2V6H0z" fill="#fff"/></svg><span class="txn__phone">+39 012 555 0163</span><span class="txn__amount">€&nbsp;&nbsp;200</span><svg width="7" height="10" viewBox="0 0 7 10"><path d="M0 0l7 5-7 5z" fill="#fff"/></svg></div>
  <div class="txn" style="top:312px"><svg width="14" height="12" viewBox="0 0 14 12"><path d="M7 0l7 6h-2v6H9V8H5v4H2V6H0z" fill="#fff"/></svg><span class="txn__phone">+39 551 555 0129</span><span class="txn__amount">€&nbsp;&nbsp;12</span><svg width="7" height="10" viewBox="0 0 7 10"><path d="M0 0l7 5-7 5z" fill="#fff"/></svg></div>
  <div class="txn" style="top:349px"><svg width="14" height="12" viewBox="0 0 14 12"><path d="M7 0l7 6h-2v6H9V8H5v4H2V6H0z" fill="#fff"/></svg><span class="txn__phone">+39 340 555 0182</span><span class="txn__amount">€&nbsp;&nbsp;-1</span><svg width="7" height="10" viewBox="0 0 7 10"><path d="M0 0l7 5-7 5z" fill="#fff"/></svg></div>
  <div class="txn" style="top:386px"><svg width="14" height="12" viewBox="0 0 14 12"><path d="M7 0l7 6h-2v6H9V8H5v4H2V6H0z" fill="#fff"/></svg><span class="txn__phone">+39 012 555 0163</span><span class="txn__amount">€&nbsp;&nbsp;200</span><svg width="7" height="10" viewBox="0 0 7 10"><path d="M0 0l7 5-7 5z" fill="#fff"/></svg></div>
  <div class="txn" style="top:423px"><svg width="14" height="12" viewBox="0 0 14 12"><path d="M7 0l7 6h-2v6H9V8H5v4H2V6H0z" fill="#fff"/></svg><span class="txn__phone">+39 551 555 0129</span><span class="txn__amount">€&nbsp;&nbsp;12</span><svg width="7" height="10" viewBox="0 0 7 10"><path d="M0 0l7 5-7 5z" fill="#fff"/></svg></div>

  <a class="btn btn--report">Report</a>
  <a class="btn btn--pockets">Tasche</a>
</section>

</main>
</body>
</html>
```